Pixvane Set Up Ads for KELBY Property Management Company

We need a set of 6 ads of the following sizes created for Pixvane:

Medium rectangle: 300×250
Leaderboard: 728×90
Wide skyscraper: 160×600
Large rectangle: 300x600
Mobile leaderboard: 320×50
Billboard: 970x250

Here are the Formatting Guidelines (WEB ADS): https://help.pixvane-example.com/hc/en-us/articles/583920174-Ad-Content-and-Format-Guidelines

No animation - photos to link back to the website.

Here is the website: https://www.kelbyrenews-example.com/

Please try to copy the look and feel.

Here are some words for the ad - feel free to use creative liberties if you have something better or need less words.

1. KELBY. Results - Not Recommendations.
2. KELBY. Transform Your Business By Transforming Your Core.
3. It's time for better results. It's time to change your management company. KELBY.
4. What company couldn't benefit from a "fresh set of eyes?" Talk to Kelby.
5. Talk to KELBY about what they can do for your bottom-line.

Target Market(s)

People who have already visited our website. These people will be private owners, REITs, or Private Equity people looking for a new management company for their underperforming asset.

Industry/Entity Type

Property Management

Font styles to use
Sans Serif

Colors
f37122
6b449b
33b8a4

Requirements
Must have
• logo - at least the "O" unless you can find other ways to pull it back to the website.
Nice to have
• Photos from kelbyrenews-example.com to remind the user what website we are when they are redirected - I purchased from lumbra photos off tilde grove.
Should not have
• Animation

```html
<!DOCTYPE html>
<html lang="en">
<head>
<meta charset="utf-8">
<title>KELBY display ad set</title>
<link href="https://fonts.googleapis.com/css2?family=Open+Sans:wght@400;700&display=swap" rel="stylesheet">
<style>
  :root {
    --stage-light: #f2f2f2;
    --stage-dark: #c9c9c9;
    --header-white: #ffffff;
    --brand-purple: #3b1f4f;
    --text-light: #ffffff;
    --frame-line: rgba(255, 255, 255, 0.75);
    --wood-warm: #9a5f2a;
    --wood-light: #a88a6a;
    --stone-grey: #5e5a56;
    --shadow: rgba(0, 0, 0, 0.35);
  }
  * { box-sizing: border-box; margin: 0; padding: 0; }
  html, body { width: 1200px; height: 1200px; overflow: hidden; }
  body {
    font-family: "Open Sans", Arial, sans-serif;
    background: radial-gradient(circle at 50% 45%, var(--stage-light) 0%, var(--stage-dark) 75%);
    position: relative;
  }
  .ad {
    position: absolute;
    overflow: hidden;
    box-shadow: 0 8px 10px -4px var(--shadow);
  }
  .ad-photo { position: absolute; inset: 0; }
  .photo-tangram-table {
    background:
      linear-gradient(rgba(40, 32, 26, 0.35), rgba(40, 32, 26, 0.45)),
      linear-gradient(90deg, var(--stone-grey) 0%, var(--stone-grey) 18%, var(--wood-warm) 30%, var(--wood-warm) 78%, var(--stone-grey) 90%);
  }
  .photo-tangram-square {
    background:
      linear-gradient(rgba(40, 32, 26, 0.35), rgba(40, 32, 26, 0.5)),
      radial-gradient(ellipse at 50% 35%, var(--wood-warm) 0%, var(--wood-warm) 35%, var(--stone-grey) 70%);
  }
  .photo-tangram-pieces {
    background:
      linear-gradient(rgba(40, 32, 26, 0.45), rgba(30, 26, 24, 0.55)),
      linear-gradient(160deg, #8a6e58 0%, #6b5a4b 45%, #4a4e55 100%);
  }
  .photo-tangram-stack {
    background:
      linear-gradient(rgba(40, 32, 26, 0.4), rgba(20, 18, 16, 0.5)),
      linear-gradient(180deg, #6a6560 0%, #6a6560 15%, var(--wood-light) 30%, var(--wood-light) 88%, #2a2622 92%, #2a2622 100%);
  }
  .ad-header {
    position: absolute;
    top: 0; left: 0; right: 0;
    background: var(--header-white);
    display: flex;
    align-items: center;
    justify-content: center;
    gap: 6px;
    border-bottom-right-radius: 60px 100%;
    box-shadow: 0 2px 3px rgba(0,0,0,0.25);
  }
  .brand-dot {
    width: 22px; height: 22px;
    border-radius: 50%;
    background: var(--brand-purple);
  }
  .brand-name {
    font-weight: 700;
    color: var(--brand-purple);
    font-size: 20px;
    letter-spacing: 0.5px;
  }
  .message-frame {
    position: absolute;
    border: 1px solid var(--frame-line);
    display: flex;
    align-items: center;
    justify-content: center;
    text-align: center;
    color: var(--text-light);
    line-height: 1.2;
    white-space: nowrap;
  }

  /* Leaderboard */
  .ad-leaderboard { left: 309px; top: 279px; width: 582px; height: 71px; }
  .ad-leaderboard .ad-header {
    right: auto; width: 134px; height: 71px;
    border-bottom-right-radius: 70px 100%;
    box-shadow: none;
  }
  .ad-leaderboard .brand-dot { width: 20px; height: 20px; }
  .ad-leaderboard .brand-name { font-size: 17px; }
  .ad-leaderboard .message-frame {
    left: 145px; top: 13px; width: 425px; height: 46px;
    font-size: 16.5px;
  }

  /* Large rectangle */
  .ad-large { left: 245px; top: 480px; width: 240px; height: 480px; }
  .ad-large .ad-header { height: 52px; }
  .ad-large .message-frame {
    left: 20px; top: 83px; width: 200px; height: 371px;
    font-size: 19px; line-height: 1.22;
  }

  /* Wide skyscraper */
  .ad-skyscraper { left: 538px; top: 480px; width: 128px; height: 480px; }
  .ad-skyscraper .ad-header { height: 58px; border-bottom-right-radius: 36px 100%; }
  .ad-skyscraper .brand-dot { width: 18px; height: 18px; }
  .ad-skyscraper .brand-name { font-size: 16px; }
  .ad-skyscraper .message-frame {
    left: 10px; top: 70px; width: 107px; height: 397px;
    font-size: 19px; line-height: 1.22;
  }

  /* Medium rectangle */
  .ad-medium { left: 715px; top: 480px; width: 240px; height: 200px; }
  .ad-medium .ad-header { height: 46px; }
  .ad-medium .brand-name { font-size: 19px; }
  .ad-medium .message-frame {
    left: 10px; top: 66px; width: 219px; height: 118px;
    font-size: 16.5px; line-height: 1.22;
  }
</style>
</head>
<body>

  <section class="ad ad-leaderboard">
    <div class="ad-photo photo-tangram-table" role="img" aria-label="Photo of wooden tangram pieces on a grey stone surface"></div>
    <header class="ad-header">
      <span class="brand-dot"></span><span class="brand-name">KELBY</span>
    </header>
    <p class="message-frame">Transform Your Business By Transforming Your Core</p>
  </section>

  <section class="ad ad-large">
    <div class="ad-photo photo-tangram-pieces" role="img" aria-label="Photo of coloured tangram pieces scattered on a wooden table"></div>
    <header class="ad-header">
      <span class="brand-dot"></span><span class="brand-name">KELBY</span>
    </header>
    <p class="message-frame">What company<br>couldn't benefit<br>from a "fresh set<br>of eyes?" Talk to<br>Kelby.</p>
  </section>

  <section class="ad ad-skyscraper">
    <div class="ad-photo photo-tangram-stack" role="img" aria-label="Photo of a wooden tangram puzzle on a stone surface"></div>
    <header class="ad-header">
      <span class="brand-dot"></span><span class="brand-name">KELBY</span>
    </header>
    <p class="message-frame">It's time<br>for better<br>results. It's<br>time to<br>change<br>your<br>manage-<br>ment<br>company.</p>
  </section>

  <section class="ad ad-medium">
    <div class="ad-photo photo-tangram-square" role="img" aria-label="Photo of a wooden tangram puzzle on a grey stone surface"></div>
    <header class="ad-header">
      <span class="brand-dot"></span><span class="brand-name">KELBY</span>
    </header>
    <p class="message-frame">It's time for better re-<br>sults. It's time to change<br>your management com-<br>pany.</p>
  </section>

</body>
</html>
```